Business Card Design for Corvella

Need a business card designed for Corvella employees.
- 2 sided business card
- Front:
Company Logo (file attached)
Background could be:white with perhaps a red/black stripe on the left
OR
Background could be: OR dark red-black gradient: be creative
Include the following on the front:
Marcus Dellow
Founder & CEO
marcus.dellow@corvella-example.com
+1 555.010.0147
corvella-example.com
- Back: White color background with company logo
Text under the logo: Invoice Automation 2.0
** be creative about the font, mix of upper and lower case and colors for the text **
Target Market(s)
We are a software company marketing our products to large and medium sized businesses.
Industry/Entity Type
Business

```html
<!DOCTYPE html>
<html lang="en">
<head>
<meta charset="utf-8">
<title>Corvella Business Card</title>
<link rel="stylesheet" href="https://fonts.googleapis.com/css2?family=Open+Sans:wght@300;400;700&display=swap">
<style>
  :root {
    --page-bg: #e6e6e8;
    --card-bg: #ffffff;
    --ink: #2b2b2b;
    --ink-soft: #3c3c3c;
    --brand-red: #c8161d;
    --brand-orange: #f07a1a;
    --deep-red: #6e0c10;
    --swoosh-grey: #9a9a9a;
    --divider: #b0252a;
  }
  * { box-sizing: border-box; margin: 0; padding: 0; }
  html, body {
    width: 1200px;
    height: 1000px;
    overflow: hidden;
    background: var(--page-bg);
    font-family: "Open Sans", Arial, sans-serif;
  }
  .card {
    position: absolute;
    left: 215px;
    width: 770px;
    height: 440px;
    background: var(--card-bg);
    overflow: hidden;
    box-shadow: 0 6px 18px rgba(0,0,0,0.18);
  }
  .card--back { top: 40px; }
  .card--front { top: 520px; }
  .card__swoosh {
    position: absolute;
    inset: 0;
    width: 100%;
    height: 100%;
  }
  .brand {
    position: absolute;
    display: flex;
    align-items: center;
    gap: 18px;
  }
  .brand__dot {
    border-radius: 50%;
    background: var(--brand-red);
    flex: none;
  }
  .brand__name {
    font-weight: 300;
    color: var(--ink);
    letter-spacing: 0.08em;
    text-transform: uppercase;
    line-height: 1;
  }
  .card--back .brand { left: 110px; top: 145px; }
  .card--back .brand__dot { width: 92px; height: 92px; }
  .card--back .brand__name { font-size: 76px; }

  .tagline {
    position: absolute;
    left: 222px;
    top: 252px;
    font-size: 20px;
    font-weight: 400;
    letter-spacing: 0.04em;
    color: var(--ink-soft);
    line-height: 1.2;
  }

  .card--front .brand { left: 40px; top: 170px; gap: 12px; }
  .card--front .brand__dot { width: 56px; height: 56px; }
  .card--front .brand__name { font-size: 42px; }

  .divider {
    position: absolute;
    left: 428px;
    top: 40px;
    width: 2px;
    height: 250px;
    background: linear-gradient(to bottom, rgba(176,37,42,0.1), var(--divider) 50%, rgba(80,80,80,0.6));
  }
  .person {
    position: absolute;
    left: 455px;
    top: 62px;
  }
  .person__name {
    color: var(--brand-red);
    font-weight: 700;
    font-size: 21px;
    line-height: 1.2;
  }
  .person__title {
    color: var(--ink);
    font-weight: 700;
    font-size: 14px;
    margin-top: 4px;
  }
  .contact {
    position: absolute;
    left: 455px;
    top: 170px;
    list-style: none;
  }
  .contact__item {
    display: flex;
    align-items: center;
    gap: 8px;
    font-size: 14px;
    color: var(--ink-soft);
    height: 30px;
    white-space: nowrap;
  }
  .contact__icon { width: 22px; height: 22px; flex: none; }
</style>
</head>
<body>

<section class="card card--back" aria-label="Card back">
  <svg class="card__swoosh" viewBox="0 0 770 440" preserveAspectRatio="none" aria-hidden="true">
    <defs>
      <linearGradient id="backBand" x1="0" y1="1" x2="1" y2="0">
        <stop offset="0" stop-color="#c8161d"/>
        <stop offset="0.6" stop-color="#e2401b"/>
        <stop offset="1" stop-color="#f07a1a"/>
      </linearGradient>
    </defs>
    <path d="M300,440 Q560,380 770,215" fill="none" stroke="#9a9a9a" stroke-width="4"/>
    <path d="M360,440 Q590,390 770,232 L770,440 Z" fill="url(#backBand)"/>
  </svg>
  <div class="brand">
    <span class="brand__dot"></span>
    <span class="brand__name">Corvella</span>
  </div>
  <p class="tagline">Invoice Automation 2.0</p>
</section>

<section class="card card--front" aria-label="Card front">
  <svg class="card__swoosh" viewBox="0 0 770 440" preserveAspectRatio="none" aria-hidden="true">
    <defs>
      <linearGradient id="frontBand" x1="0" y1="0" x2="1" y2="0">
        <stop offset="0" stop-color="#f07a1a"/>
        <stop offset="0.3" stop-color="#d9231d"/>
        <stop offset="0.7" stop-color="#6e0c10"/>
        <stop offset="1" stop-color="#0d0d0d"/>
      </linearGradient>
    </defs>
    <path d="M0,385 Q420,340 770,250" fill="none" stroke="#a0a0a0" stroke-width="5"/>
    <path d="M0,400 Q420,356 770,266 L770,440 L0,440 Z" fill="url(#frontBand)"/>
  </svg>

  <div class="brand">
    <span class="brand__dot"></span>
    <span class="brand__name">Corvella</span>
  </div>

  <div class="divider"></div>

  <div class="person">
    <p class="person__name">Marcus Dellow</p>
    <p class="person__title">Founder &amp; CEO</p>
  </div>

  <ul class="contact">
    <li class="contact__item">
      <svg class="contact__icon" viewBox="0 0 22 22" aria-hidden="true">
        <rect x="2" y="5" width="18" height="12" rx="1" fill="#eee" stroke="#888"/>
        <path d="M2,5 L11,12 L20,5" fill="none" stroke="#888"/>
      </svg>
      <span>: marcus.dellow@corvella-example.com</span>
    </li>
    <li class="contact__item">
      <svg class="contact__icon" viewBox="0 0 22 22" aria-hidden="true">
        <rect x="6" y="2" width="10" height="18" rx="2" fill="#555"/>
        <rect x="7.5" y="4" width="7" height="11" fill="#ccc"/>
        <circle cx="11" cy="17.5" r="1" fill="#ccc"/>
      </svg>
      <span>: +1 555.010.0147</span>
    </li>
    <li class="contact__item">
      <svg class="contact__icon" viewBox="0 0 22 22" aria-hidden="true">
        <circle cx="11" cy="11" r="8.5" fill="#ddd" stroke="#777"/>
        <ellipse cx="11" cy="11" rx="4" ry="8.5" fill="none" stroke="#777"/>
        <line x1="2.5" y1="11" x2="19.5" y2="11" stroke="#777"/>
      </svg>
      <span>: corvella-example.com</span>
    </li>
  </ul>
</section>

</body>
</html>
```